Custom Cabinet Shop Needs a website design

Hi,
We need a website for a Custom Cabinet Shop and Cabinet parts manufacturing business.
The business has two sides to it. One side provides custom Kitchens, vanities, entertainment units, offices and what not to homeowners and contractors.
The 2nd side of the business provides built to order cabinet boxes and other parts required to put together a project to other cabinet shops, small contractors looking to install there own cabinets.
Website will need a Gallery to display work.
Color scheme to go well with logo.
current website is www.brindlewoodcustomcabinets.com
being changed to www.brindlewood.ca
Logo Included in attached files.
Tagline "Millwork with Flare"
Mission Statement "Our passion is to deliver inspired cabinetry solutions to suit all your needs, supported by our phenomenal star class customer service"
The website should convey quality and professionalism.
Thank you.
Homeowners/ Contractors
Entertainment
Coded - Design and coding required
1 page

```html
<!DOCTYPE html>
<html lang="en">
<head>
<meta charset="utf-8">
<title>Brindlewood Custom Cabinets</title>
<link href="https://fonts.googleapis.com/css2?family=Raleway:wght@400;500;600&family=Montserrat:wght@600;700;800&family=Arimo:wght@400&display=swap" rel="stylesheet">
<style>
:root{
  --orange:#f15a24;
  --dark:#222;
  --mid-bg:#f3f3f3;
  --foot-bg:#e9e9e9;
  --text:#333;
  --line:#b9b9b9;
}
*{box-sizing:border-box;margin:0;padding:0}
html,body{width:1159px;height:1200px;overflow:hidden}
body{font-family:"Raleway",sans-serif;color:var(--text);background:var(--mid-bg);position:relative}
.wrap{position:absolute;left:109px;width:944px}

.header{position:absolute;top:0;left:0;width:1159px;height:128px;background:linear-gradient(#2a2a2a,#1e1e1e)}
.brand{top:44px;display:flex;align-items:center;gap:10px}
.brand-mark{width:34px;height:34px;background:var(--orange);border-radius:50%}
.brand-name{font-family:"Montserrat",sans-serif;font-weight:800;font-size:31px;color:#fff;letter-spacing:.5px}
.phone{position:absolute;right:0;top:49px;display:flex;align-items:center;gap:9px;color:var(--orange);font-size:22px;font-weight:500}

.nav{position:absolute;top:128px;left:0;width:1159px;height:57px;background:linear-gradient(#fafafa,#e6e6e6);border-bottom:2px solid #1a1a1a}
.nav ul{list-style:none;display:flex;height:57px}
.nav li{padding:0 21px;font-size:16px;font-weight:500;color:#222;border-right:1px solid #d4d4d4;height:48px;margin-top:4px;line-height:48px;white-space:nowrap}
.nav li:last-child{border:0}
.nav li.active{background:var(--orange);color:#fff;margin-top:0;height:57px;line-height:57px;padding:0 10px;border:0}
.social{position:absolute;right:0;top:12px;display:flex;gap:8px}
.social span{width:39px;height:36px;display:block}

.hero-band{position:absolute;top:186px;left:0;width:1159px;height:417px;background:#1c1c1c}
.slide{top:20px;height:397px;background:linear-gradient(100deg,#2d3442 0%,#5a4a3a 40%,#8a6a4a 65%,#6b5641 100%)}
.caption{position:absolute;left:0;top:109px;width:368px;height:231px;background:rgba(20,20,20,.78);padding:16px 18px}
.caption h1{font-weight:400;font-size:35px;line-height:42px;color:#fff;white-space:nowrap;letter-spacing:-.2px}
.caption h1 em{font-style:normal;color:var(--orange)}
.caption p{font-size:14px;color:#fff;line-height:18px;margin-top:4px;letter-spacing:-.3px}
.btn{display:inline-block;background:var(--orange);color:#fff;font-size:16px;font-weight:500;padding:9px 15px;margin-top:16px}
.dots{display:flex;gap:9px;margin-top:24px}
.arrow{position:absolute;top:178px;width:29px;height:56px;background:#111}

.mid{position:absolute;top:603px;left:0;width:1159px;height:344px;background:var(--mid-bg)}
h2{font-family:"Montserrat",sans-serif;font-weight:700;font-size:21px;color:#222;white-space:nowrap}
.chat{position:absolute;left:0;top:44px;width:304px;height:266px;background:#fff;padding:8px}
.chat-in{background:#f7f7f7;height:100%;padding:6px 8px}
.chat p{font-size:14px;margin:6px 0 12px;white-space:nowrap}
.field{background:#fff;border:1px solid #ccc;border-radius:3px;font-size:13px;color:#888;padding:11px 9px;margin-bottom:12px}
.submit{display:inline-block;background:var(--orange);color:#fff;font-family:"Montserrat",sans-serif;font-weight:800;font-size:16px;padding:9px 18px}
.says{position:absolute;left:322px;top:58px;width:340px}
.quote{display:flex;gap:10px;margin-top:24px;font-family:"Arimo",sans-serif}
.avatar{flex:none;width:82px;height:70px;border:1px solid #ccc;background:#fff;padding:4px}
.avatar div{width:100%;height:100%;background:linear-gradient(#8a7a6a,#4b3e34)}
.quote p{font-size:12px;color:#555;line-height:18px;text-align:center;width:236px}
.quote b{display:block;font-weight:400;color:#111;text-align:right;font-size:12.5px}
.video{position:absolute;left:676px;top:58px;width:268px}
.player{margin-top:22px;height:184px;background:linear-gradient(#b0b0b0,#6d3a24 45%,#4d2818);position:relative}
.play{position:absolute;left:96px;top:66px;width:74px;height:48px;background:#111;border-radius:8px}
.play:after{content:"";position:absolute;left:28px;top:12px;border-left:22px solid #fff;border-top:12px solid transparent;border-bottom:12px solid transparent}
.bar{position:absolute;bottom:0;left:0;right:0;height:18px;background:#111}

.footer{position:absolute;top:947px;left:0;width:1159px;height:253px;background:var(--foot-bg);border-top:1px solid #d6d6d6}
.col{position:absolute;top:38px}
.links{margin-top:15px;border-top:1px dotted var(--line);display:grid;grid-template-columns:141px 1fr}
.links.shop{grid-template-columns:132px 1fr}
.links span{font-size:13.5px;font-weight:500;color:#333;height:32px;line-height:31px;border-bottom:1px dotted var(--line);padding-left:1px;white-space:nowrap}
.soc span{display:flex;align-items:center;gap:8px}
.soc i{width:20px;height:20px;display:block}
.credit{position:absolute;right:0;top:70px;width:178px;font-size:13.5px;line-height:20px;color:#222;white-space:nowrap}
.credit .name{font-family:"Montserrat",sans-serif;font-weight:800;font-size:18px;display:flex;align-items:center;gap:6px;margin-bottom:12px}
.credit .name b{width:16px;height:16px;background:var(--orange);border-radius:50%}
</style>
</head>
<body>
<header class="header">
  <div class="wrap brand"><span class="brand-mark"></span><span class="brand-name">BRINDLEWOOD</span></div>
  <div class="wrap" style="top:0;height:128px">
    <div class="phone">
      <svg width="34" height="34" viewBox="0 0 34 34"><circle cx="17" cy="17" r="15.5" fill="none" stroke="#fff" stroke-width="1.6"/><path d="M12 9c1 0 3 4 2 5s-2 1-1 3 3 4 5 5 2 0 3-1 5 1 5 2-2 3-4 3C16 26 8 18 8 13c0-2 3-4 4-4z" fill="#fff"/></svg>
      403-555-0148
    </div>
  </div>
</header>

<nav class="nav">
  <div class="wrap" style="top:0">
    <ul><li class="active">HOME</li><li>GALLERY</li><li>SERVICES</li><li>WARRANTY</li><li>CONTACT</li></ul>
    <div class="social"><span style="background:#4ab3e8"></span><span style="background:#3b67b5"></span><span style="background:#e0473a"></span><span style="background:#f5a21b"></span></div>
  </div>
</nav>

<section class="hero-band">
  <div class="wrap slide" role="img" aria-label="Photo of a finished basement bar with live-edge counter, stools and dark cabinetry">
    <div class="caption">
      <h1>Millwork <em>with Flare</em></h1>
      <p>Our passion is to deliver inspired cabinetry solutions to suit all your needs, supported by our phenomenal star class customer service</p>
      <span class="btn">Read More</span>
      <div class="dots">
        <svg width="20" height="18" viewBox="0 0 20 18"><path d="M10 1l2.5 6H19l-5.2 4 2 6L10 13.3 4.2 17l2-6L1 7h6.5z" fill="none" stroke="#fff" stroke-width="1.3"/></svg>
        <svg width="20" height="18" viewBox="0 0 20 18"><path d="M10 1l2.5 6H19l-5.2 4 2 6L10 13.3 4.2 17l2-6L1 7h6.5z" fill="none" stroke="#f15a24" stroke-width="1.3"/></svg>
        <svg width="20" height="18" viewBox="0 0 20 18"><path d="M10 1l2.5 6H19l-5.2 4 2 6L10 13.3 4.2 17l2-6L1 7h6.5z" fill="none" stroke="#fff" stroke-width="1.3"/></svg>
        <svg width="20" height="18" viewBox="0 0 20 18"><path d="M10 1l2.5 6H19l-5.2 4 2 6L10 13.3 4.2 17l2-6L1 7h6.5z" fill="none" stroke="#fff" stroke-width="1.3"/></svg>
      </div>
    </div>
  </div>
  <div class="arrow" style="left:62px"><svg width="29" height="56"><path d="M18 16l-7 12 7 12" fill="none" stroke="#f15a24" stroke-width="1.5"/></svg></div>
  <div class="arrow" style="left:1073px"><svg width="29" height="56"><path d="M11 16l7 12-7 12" fill="none" stroke="#f15a24" stroke-width="1.5"/></svg></div>
</section>

<section class="mid">
  <div class="wrap" style="top:0;height:344px">
    <div class="chat"><div class="chat-in">
      <h2>LIVE CHAT</h2>
      <p>Have some Question? Use Online Chat.</p>
      <div class="field">Your name</div>
      <div class="field" style="height:66px">Your question</div>
      <span class="submit">SUBMIT</span>
    </div></div>
    <div class="says">
      <h2>WHAT OUR CUSTOMERS SAY:</h2>
      <div class="quote"><div class="avatar"><div role="img" aria-label="Customer portrait"></div></div>
        <p>When one of the top homebuilders in Kansas City chooses your cabinets for his personal home, then you know you<b>Owen Blake</b></p></div>
      <div class="quote" style="margin-top:30px"><div class="avatar"><div role="img" aria-label="Customer portrait"></div></div>
        <p>It was originally constructed in Ireland. Then shipped to a bar in Grand Cayman. And now, more at:<b style="padding-right:20px">Marty L.</b></p></div>
    </div>
    <div class="video">
      <h2>WATCH OUR VIDEO</h2>
      <div class="player" role="img" aria-label="Video still of a cherry wood kitchen with island"><span class="play"></span><span class="bar"></span></div>
    </div>
  </div>
</section>

<footer class="footer">
  <div class="wrap" style="top:0;height:253px">
    <div class="col" style="left:0;width:268px"><h2>NAVIGATION</h2>
      <div class="links"><span>Home</span><span>Free Door Sample</span><span>Gallery</span><span>FAQ</span><span>Services</span><span>Contact us</span><span>Warranty</span><span></span></div></div>
    <div class="col" style="left:314px;width:268px"><h2>SHOP NOW</h2>
      <div class="links shop"><span>&nbsp;Kitchen Cabinet</span><span>Terms And Conditions</span><span>&nbsp;Countertops</span><span>Privancy Policy</span><span>&nbsp;Bath Cabinets</span><span></span><span style="grid-column:span 2">&nbsp;Surplus Designer Sale</span></div></div>
    <div class="col" style="left:625px;width:114px"><h2>SOCIAL</h2>
      <div class="links soc" style="grid-template-columns:1fr">
        <span><i style="background:#1da1e0"></i>Chirpline</span>
        <span><i style="background:#3b5998"></i>Friendbook</span>
        <span><i style="background:#ccc"></i>Circles+</span>
        <span><i style="background:#2bb24c"></i>RSS Feed</span></div></div>
    <div class="credit"><div class="name"><b></b>BRINDLEWOOD</div>© 2023 by Lena Ortiz.<br>Proudly created with Sitecraft.io</div>
  </div>
</footer>
</body>
</html>
```